Simple proffessional BC

I have a logo which I will attach below.
I would like the logo on the front of the card with these details in point form below:
Pre and Post Natal Yoga: Pregnancy Workshops: Hypnobirthing Courses
On the back of the card my details:
Merrin Galvey
Facebook page- calmbellieswillowharbour
Mobile- 0438 512 740

I like the idea of the card being simple, possibly just the above on a plain coloured (eggshell?) card, a card that is textured.
I am open to suggestion if it appeals!
Thank you and good luck!

Target Market(s)

Pregnant women, 20's-40's

Requirements
Must have
• Simple, compliment logo.
Make logo the feature.
Should not have

• .

```html
<!DOCTYPE html>
<html lang="en">
<head>
<meta charset="utf-8">
<title>Calm Bellies – Business Card</title>
<link rel="stylesheet" href="https://fonts.googleapis.com/css2?family=Questrial&display=swap">
<style>
  :root {
    --maroon: #5e1412;
    --saffron: #eba33a;
    --eggshell: #fbefe3;
    --ink: #6a1a1a;
    --backdrop: #e9e4dc;
  }
  * { margin: 0; padding: 0; box-sizing: border-box; }
  html, body {
    width: 1200px; height: 1024px; overflow: hidden;
    background: var(--backdrop);
    font-family: "Questrial", "Century Gothic", sans-serif;
  }
  .sheet {
    width: 1200px; height: 1024px;
    display: flex; flex-direction: column; align-items: center;
    justify-content: center; gap: 32px;
  }
  .card {
    width: 840px; height: 480px; position: relative;
    box-shadow: 0 6px 18px rgba(0,0,0,.18);
  }
  /* Front */
  .card--front { background: var(--maroon); }
  .front-mark {
    position: absolute; left: 50%; top: 58px; transform: translateX(-50%);
    display: flex; flex-direction: column; align-items: center; gap: 22px;
  }
  .front-mark__disc {
    width: 250px; height: 250px; border-radius: 50%; background: var(--saffron);
  }
  .front-mark__name { color: var(--saffron); font-size: 34px; letter-spacing: .5px; }
  .services {
    position: absolute; left: 0; right: 36px; bottom: 26px;
    text-align: right; color: var(--saffron); font-size: 15px; letter-spacing: .3px;
  }
  /* Back */
  .card--back { background: var(--eggshell); color: var(--ink); }
  .back-mark {
    position: absolute; left: 78px; top: 52px;
    display: flex; align-items: center; gap: 20px;
  }
  .back-mark__disc { width: 96px; height: 96px; border-radius: 50%; background: var(--saffron); }
  .back-mark__name { font-size: 64px; color: var(--ink); }
  .person {
    position: absolute; left: 194px; top: 178px; font-size: 40px;
  }
  .contacts {
    position: absolute; left: 84px; top: 290px;
    list-style: none; display: flex; flex-direction: column; gap: 26px;
  }
  .contacts__item { display: flex; align-items: center; gap: 14px; font-size: 28px; }
  .contacts__icon {
    width: 30px; height: 30px; border-radius: 50%; background: var(--saffron);
    display: flex; align-items: center; justify-content: center; flex: none;
  }
</style>
</head>
<body>
<main class="sheet">
  <section class="card card--front" aria-label="Card front">
    <div class="front-mark">
      <div class="front-mark__disc"></div>
      <div class="front-mark__name">Calm Bellies</div>
    </div>
    <p class="services">Pre and Post Natal Yoga | Pregnancy Workshops | Hypnobirthing Courses</p>
  </section>

  <section class="card card--back" aria-label="Card back">
    <div class="back-mark">
      <div class="back-mark__disc"></div>
      <div class="back-mark__name">Calm Bellies</div>
    </div>
    <p class="person">Merrin Galvey</p>
    <ul class="contacts">
      <li class="contacts__item contacts__item--phone">
        <span class="contacts__icon">
          <svg width="14" height="18" viewBox="0 0 14 18" aria-hidden="true">
            <rect x="1.5" y="1" width="11" height="16" rx="2" fill="none" stroke="#5e1412" stroke-width="1.6"/>
            <line x1="5.5" y1="14" x2="8.5" y2="14" stroke="#5e1412" stroke-width="1.4"/>
          </svg>
        </span>
        0438 512 740
      </li>
      <li class="contacts__item contacts__item--social">
        <span class="contacts__icon"></span>
        calmbellieswillowharbour
      </li>
    </ul>
  </section>
</main>
</body>
</html>
```